We would like to incorporate our logo into letterhead design and envelopes. We are looking for something that is moderately conservative but not old law firm style. Both the envelopes and the letterhead must have both firm addresses. We would like to incorporate the color of the logo, but only a small amount of color - perhaps on one of the borders. The addresses for the firm locations are listed below. Given that it is a law firm, it needs to somewhat conservative, but not the old school, small black font on cream colored paper design.

The firm addresses are:

27815 N. Harlow Pemberton Pkwy.
Ste 4200
Scottsdale, AZ 85391

6100 W. Cedar Avenue
Ste 700
Burbank, CA 91623

Industry/Entity Type

Legal

Colors

Designer to choose colors to be used in the design.

Requirements
Must have
• Both addresses:
• 27815 N. Harlow Pemberton Pkwy.
• Ste 4200
• Scottsdale, AZ 85391
• 6100 W. Cedar Avenue
• Ste 700
• Burbank, CA 91623
Nice to have
• Small amount of color on border(s) that matches the logo but not too much color

```html
<!DOCTYPE html>
<html lang="en">
<head>
<meta charset="utf-8">
<title>Calloway Law — Letterhead and Envelope</title>
<link href="https://fonts.googleapis.com/css2?family=Marcellus&family=Open+Sans:wght@400;600&display=swap" rel="stylesheet">
<style>
  :root {
    --backdrop: #c3c3c3;
    --paper: #f8f2e2;
    --navy: #2b275b;
    --ink: #2e2c33;
    --crease: #e2d9c4;
  }
  html, body {
    margin: 0;
    padding: 0;
    width: 1200px;
    height: 1199px;
    overflow: hidden;
    background: var(--backdrop);
  }
  .stage {
    position: relative;
    width: 1200px;
    height: 1199px;
  }
  .sheet {
    position: absolute;
    background: var(--paper);
    box-shadow: 0 1px 3px rgba(0,0,0,0.18);
  }
  .brand-band {
    position: absolute;
    top: 0;
    background: var(--navy);
    display: flex;
    align-items: center;
    justify-content: center;
    box-sizing: border-box;
    padding-left: 6px;
    padding-right: 6px;
  }
  .brand-name {
    font-family: "Marcellus", serif;
    color: var(--paper);
    letter-spacing: 0;
    white-space: nowrap;
    line-height: 1;
  }
  address { font-style: normal; }

  /* Letterhead */
  .letterhead {
    left: 135px;
    top: 288px;
    width: 452px;
    height: 639px;
  }
  .letterhead .brand-band {
    left: 149px;
    width: 153px;
    height: 57px;
    padding-top: 12px;
  }
  .letterhead .brand-name { font-size: 15px; }
  .letterhead-footer {
    position: absolute;
    left: 132px;
    top: 602px;
    display: flex;
    font-family: "Open Sans", sans-serif;
    font-size: 6px;
    line-height: 1.35;
    color: var(--ink);
  }
  .letterhead-footer .office { padding-right: 8px; }
  .letterhead-footer .office + .office {
    padding-left: 9px;
    border-left: 0.6px solid var(--ink);
  }

  /* Envelope back */
  .envelope-back {
    left: 638px;
    top: 451px;
    width: 456px;
    height: 227px;
  }
  .envelope-back svg {
    position: absolute;
    inset: 0;
  }

  /* Envelope front */
  .envelope-front {
    left: 638px;
    top: 702px;
    width: 456px;
    height: 227px;
  }
  .envelope-front .brand-band {
    left: 29px;
    width: 137px;
    height: 43px;
    padding-top: 6px;
  }
  .envelope-front .brand-name { font-size: 13.5px; }
  .return-address {
    position: absolute;
    left: 182px;
    top: 17px;
    display: flex;
    font-family: "Open Sans", sans-serif;
    font-size: 4.6px;
    line-height: 1.3;
    color: var(--ink);
  }
  .return-address .office { padding-right: 5px; }
  .return-address .office + .office {
    padding-left: 5px;
    border-left: 0.6px solid var(--ink);
  }
  .office-label { color: var(--navy); display: block; }
</style>
</head>
<body>
<main class="stage">

  <section class="sheet letterhead" aria-label="Letterhead">
    <div class="brand-band"><span class="brand-name">CALLOWAY LAW</span></div>
    <footer class="letterhead-footer">
      <address class="office">27815 N. Harlow Pemberton Pkwy.<br>Ste 4200, Scottsdale, AZ 85391</address>
      <address class="office">6100 W. Cedar Avenue<br>Ste 700, Burbank, CA 91623</address>
    </footer>
  </section>

  <section class="sheet envelope-back" aria-label="Envelope back">
    <svg width="456" height="227" viewBox="0 0 456 227">
      <path d="M1 1 L10 28 Q14 34 22 37 L200 96 Q228 104 256 96 L434 34 L455 1"
            fill="none" stroke="var(--crease)" stroke-width="1"/>
    </svg>
  </section>

  <section class="sheet envelope-front" aria-label="Envelope front">
    <div class="brand-band"><span class="brand-name">CALLOWAY LAW</span></div>
    <div class="return-address">
      <address class="office"><span class="office-label">Address1:</span>27815 N. Harlow Pemberton Pkwy.<br>Ste 4200<br>Scottsdale, AZ 85391</address>
      <address class="office"><span class="office-label">Address2:</span>6100 W. Cedar Avenue<br>Ste 700<br>Burbank, CA 91623</address>
    </div>
  </section>

</main>
</body>
</html>
```